Fenwick Law PC business card. National Consumer Law Firm with principal office in San Francisco. We maintain additional offices in Meridian, Mississippi and Birmingham, Alabama. We protect consumers against unscrupulous mega corporations. We want to covey integrity and a willingness to take on the Goliaths of the corporate world. I like red accents. Try to use uploaded picture of Harbor Arch Span or a sketch. Licensed in California, Alabama and Mississippi. Main office: 317 Alder Ave. #408, San Francisco, CA 94110, ph. 415/555-0193, 800/555-0147 (fax), 205/555-0162 (AL).
www.fenwicklawpc.example
www.buyerguard.example.
At top--Consumer Class Litigation in red. Also Fenwick Law PC at top in red. Then red horizontal line please. Or if you have another idea. I have not seen new logo.
After line on left at top
L. Thomas Fenwick
Attorney
Cell 205/555-0178
thomas@fenwicklawpc.example
Offices: San Francisco, CA, Birmingham, AL, Charlotte, NC and Meridian, MS

I asked that the very bottom of the BUSINESS CARD TO SAY "Offices in California, North Carolina, Alabama and Mississippi NOT STATES WHERE I AM LICENSED. I.E., I AM NOT LICENSED IN NOTH CAROLINA I NEED NEW FILES IF YOU CAN GET THEM IN THE MORNING MY TIME. WHERE CAN I FIND THE NEW FILES ONCE YOU MODIFY.

for North Carolina, I need an asterick where it is listed. "not licensed will associate counsel" AGAIN NORTH CAROLINA IS 2 WORDS WITH A SPACE BETWEEN THEM

For Biz card, put tollfree number (888)555-0121 and toll free fax (800)555-0147 somewhere like below my cell number or wherever you can. States where I have offices at the bottom: California, North Carolina, Alabama and Mississippi.

For Biz card, put tollfree number (888)555-0121 and toll free fax (800)555-0147 somewhere like below my cell number or wherever you can. States where I have offices at the bottom: California, North Carolina, Alabama and Mississippi. AstericK *North Carolina--not licensed will associate co-counel. Same with letterhead and website. I need to disclose not licensed to practice in North Carolina.

```html
<!DOCTYPE html>
<html lang="en">
<head>
<meta charset="utf-8">
<title>Fenwick Law PC – Business Card</title>
<link rel="stylesheet" href="https://fonts.googleapis.com/css2?family=PT+Sans+Narrow:wght@400;700&family=Arimo&display=swap">
<style>
  :root {
    --frame-red: #c8141c;
    --brand-red: #d8281f;
    --panel-cream: #eeebe1;
    --ink: #3a3531;
    --sky-top: #5f8fd6;
    --sky-mid: #b9c9e0;
    --bay-mid: #2f7f95;
    --bay-deep: #145a6c;
  }
  * { margin: 0; padding: 0; box-sizing: border-box; }
  html, body {
    width: 1200px; height: 686px; overflow: hidden;
    background: #ffffff;
  }
  .card {
    position: relative;
    width: 1200px; height: 686px;
    background: var(--frame-red);
    font-family: "PT Sans Narrow", "Arial Narrow", sans-serif;
  }
  .scene {
    position: absolute;
    left: 16px; top: 16px;
    width: 588px; height: 654px;
    background: linear-gradient(180deg,
      var(--sky-top) 0%, var(--sky-mid) 40%, #a8b6c2 48%,
      var(--bay-mid) 56%, var(--bay-deep) 100%);
  }
  .details {
    position: absolute;
    left: 604px; top: 16px;
    width: 580px; height: 654px;
    background: var(--panel-cream);
  }
  .wordmark {
    position: absolute;
    left: 200px; top: 52px;
    font-size: 54px; font-weight: 400;
    color: var(--brand-red);
    letter-spacing: 1px;
    white-space: nowrap;
    line-height: 1;
  }
  .tagline {
    position: absolute;
    left: 190px; top: 144px;
    font-size: 40px;
    color: var(--brand-red);
    white-space: nowrap;
    line-height: 1;
  }
  .offices {
    position: absolute;
    right: 640px; top: 452px;
    text-align: right;
    font-family: "Arimo", Arial, sans-serif;
    font-size: 30px; line-height: 36px;
    color: var(--brand-red);
    white-space: nowrap;
  }
  .person-name {
    position: absolute; left: 30px; top: 28px;
    font-size: 40px; color: var(--brand-red);
    line-height: 1;
  }
  .person-title {
    position: absolute; left: 30px; top: 76px;
    font-size: 36px; font-weight: 700; color: var(--ink);
    line-height: 1;
  }
  .line {
    position: absolute; left: 30px;
    font-size: 31px; color: var(--ink);
    line-height: 1; white-space: nowrap;
    display: flex; align-items: center; gap: 4px;
  }
  .line svg { width: 30px; height: 26px; flex: none; }
  .line.plain { left: 28px; }
  .disclaimer {
    position: absolute; left: 28px; top: 612px;
    font-size: 22px; color: var(--brand-red);
    line-height: 1; white-space: nowrap;
  }
</style>
</head>
<body>
  <div class="card">
    <div class="scene" role="img" aria-label="Photograph of the Harbor Arch Span suspension bridge over the bay under a blue sky"></div>

    <div class="wordmark">FENWICK LAW P.C.</div>
    <div class="tagline">Consumer Class Litigation</div>
    <div class="offices">Offices in<br>California,<br>North Carolina*,<br>Alabama and<br>Mississippi</div>

    <div class="details">
      <div class="person-name">L. Thomas Fenwick</div>
      <div class="person-title">Attorney</div>

      <div class="line" style="top:136px">
        <svg viewBox="0 0 30 26" aria-hidden="true"><circle cx="14" cy="13" r="11" fill="none" stroke="#3a3531" stroke-width="2"/><path d="M10 7c-2 3-2 9 1 12l3-2-2-3 0-2 2-2-1-3z" fill="#3a3531"/></svg>
        <span>205.555.0178 (cell)</span>
      </div>
      <div class="line" style="top:176px">
        <svg viewBox="0 0 30 26" aria-hidden="true"><path d="M2 9c6-6 20-6 26 0l-2 4-5-1V9H9v3l-5 1z" fill="#3a3531"/><path d="M6 24l3-10h12l3 10z" fill="#3a3531"/><circle cx="15" cy="18" r="3" fill="#eeebe1"/></svg>
        <span>888.555.0121 (toll free)</span>
      </div>
      <div class="line plain" style="top:218px">thomas@fenwicklawpc.example</div>

      <div class="line plain" style="top:278px">317 Alder Ave #408</div>
      <div class="line plain" style="top:316px">San Francisco, CA 94110</div>

      <div class="line" style="top:366px">
        <svg viewBox="0 0 30 26" aria-hidden="true"><path d="M2 9c6-6 20-6 26 0l-2 4-5-1V9H9v3l-5 1z" fill="#3a3531"/><path d="M6 24l3-10h12l3 10z" fill="#3a3531"/><circle cx="15" cy="18" r="3" fill="#eeebe1"/></svg>
        <span>415.555.0193</span>
      </div>
      <div class="line" style="top:406px">
        <svg viewBox="0 0 30 26" aria-hidden="true"><rect x="8" y="2" width="14" height="10" fill="none" stroke="#3a3531" stroke-width="2"/><rect x="3" y="11" width="24" height="13" fill="none" stroke="#3a3531" stroke-width="2"/><path d="M7 16h10M7 20h10" stroke="#3a3531" stroke-width="2"/></svg>
        <span>800.555.0147 (toll free fax)</span>
      </div>
      <div class="line" style="top:446px">
        <svg viewBox="0 0 30 26" aria-hidden="true"><path d="M2 9c6-6 20-6 26 0l-2 4-5-1V9H9v3l-5 1z" fill="#3a3531"/><path d="M6 24l3-10h12l3 10z" fill="#3a3531"/><circle cx="15" cy="18" r="3" fill="#eeebe1"/></svg>
        <span>205.555.0162 (AL)</span>
      </div>
      <div class="line plain" style="top:488px">www.fenwicklawpc.example</div>
      <div class="line plain" style="top:528px">www.buyerguard.example</div>

      <div class="disclaimer">*North Carolina – not licensed, will associate co-counsel</div>
    </div>
  </div>
</body>
</html>
```